Change of trading name, rebrand

existing website to be updated with new theme and logo. existing website is
www.brambleworth.com.au
Industry/Entity Type
Construction
Coding
Coded - Design and coding required
Number of Pages Required
5+ page
Requirements
Must have
- be mobile phone friendly

```html
<!DOCTYPE html>
<html lang="en">
<head>
<meta charset="utf-8">
<meta name="viewport" content="width=device-width, initial-scale=1">
<title>BWR Plant Hire – Heavy Equipment Hire</title>
<link href="https://fonts.googleapis.com/css2?family=Poppins:ital,wght@0,300;0,400;0,500;0,600;0,700;0,800;1,800&display=swap" rel="stylesheet">
<style>
:root{
  --navy:#23267a;
  --navy-deep:#1c1f66;
  --gold:#dcc062;
  --gold-light:#ecd685;
  --gold-dark:#c9a844;
  --text:#7a7a7a;
  --line:#e3e3e3;
  --mist:#d3d5e6;
  --white:#fff;
}
*{box-sizing:border-box;margin:0;padding:0}
html,body{width:1200px;height:3142px;overflow:hidden}
body{font-family:'Poppins',sans-serif;color:var(--text);background:var(--white);position:relative}
.wrap{position:absolute;left:141px;width:918px}

/* top bar */
.topbar{position:absolute;top:0;left:0;width:1200px;height:33px;background:var(--navy);color:#fff;font-size:10.5px}
.topbar .info{position:absolute;left:141px;top:0;height:33px;display:flex;align-items:center;gap:10px}
.topbar .info span{display:flex;align-items:center;gap:5px}
.topbar .sep{width:1px;height:14px;background:#fff;opacity:.7}
.topbar .social{position:absolute;right:141px;top:10px;display:flex;gap:8px}
.social i{display:block;width:13px;height:13px;background:#fff;border-radius:2px}

/* nav */
.nav{position:absolute;top:33px;left:0;width:1200px;height:83px;background:#fff}
.brand{position:absolute;left:141px;top:22px;display:flex;align-items:center;gap:8px}
.brand .mark{width:22px;height:22px;background:var(--navy)}
.brand .name{font-weight:800;font-size:24px;color:var(--navy);line-height:1}
.menu{position:absolute;right:141px;top:0;height:83px;display:flex;align-items:center;gap:26px;font-size:11.5px;color:var(--navy);font-weight:500;list-style:none}
.menu .active{color:var(--gold-dark)}

/* hero */
.hero{position:absolute;top:116px;left:0;width:1200px;height:417px;background:linear-gradient(180deg,#4b58a8 0%,#5a63a0 45%,#6b6a7a 75%,#4a4c7d 100%)}
.hero .shade{position:absolute;inset:0;background:rgba(35,38,122,.35)}
.hero h1{position:absolute;top:100px;width:100%;text-align:center;color:#fff;font-style:italic;font-weight:800;font-size:61px;letter-spacing:-1px}
.hero p{position:absolute;top:170px;width:100%;text-align:center;color:#fff;font-size:18px}
.hero .cta{position:absolute;left:433px;top:251px;width:334px;height:50px;border-radius:8px;background:linear-gradient(90deg,#d9c06a,#f3e08e,#d3b352);color:var(--navy);font-weight:800;font-size:25px;display:flex;align-items:center;justify-content:center}
.hero .dots{position:absolute;top:382px;left:0;width:100%;display:flex;justify-content:center;align-items:center;gap:9px}
.dots i{width:12px;height:12px;border:1.5px solid #fff;border-radius:50%}
.dots i.on{background:#fff}

/* about */
.about-img{position:absolute;left:141px;top:600px;width:294px;height:398px;background:linear-gradient(180deg,#4d86c8 0%,#9fc1e2 40%,#c9b48c 75%,#a38c68 100%)}
.about-text{position:absolute;left:517px;top:595px;width:542px}
h2{font-weight:700;color:var(--navy);font-size:27px;letter-spacing:.2px}
.copy{font-size:11.3px;line-height:17.5px;font-weight:300;text-align:justify}
.about-text .copy{margin-top:24px}
.about-text .copy+.copy{margin-top:18px}
.btn{display:inline-flex;align-items:center;justify-content:center;background:var(--gold);color:#fff;font-size:11px;font-weight:600;width:134px;height:42px}
.about-text .btn{margin-top:28px}

/* stats */
.stats{position:absolute;top:1065px;left:0;width:1200px;height:216px;background:var(--navy)}
.stat-card{position:absolute;left:141px;top:41px;width:918px;height:133px;background:#fff;border-radius:6px;display:flex;align-items:center}
.stat{flex:1;height:118px;border-right:1px solid #b0b0b0;display:flex;flex-direction:column;align-items:center;justify-content:flex-end;padding-bottom:8px;color:var(--navy);font-size:11px;font-weight:500;text-align:center;line-height:17px}
.stat:last-child{border:none}
.stat .icon{width:66px;height:66px;background:var(--gold);border-radius:8px;margin-bottom:auto;margin-top:4px}
.stat .num{display:flex;align-items:center;gap:6px;text-align:left}
.stat .num b{font-size:33px;font-weight:600;line-height:1}

/* fleet tabs */
.tabs{position:absolute;left:141px;top:1348px;width:918px;height:33px;background:var(--gold);display:flex;align-items:center;justify-content:center;color:#fff;font-size:13px;font-weight:600}
.tabs span{padding:0 12px;border-right:1.5px solid #fff;line-height:16px}
.tabs span:last-child{border:none}
.fleet{position:absolute;left:141px;top:1407px;width:918px;height:374px;background:#fff;box-shadow:0 0 8px rgba(0,0,0,.15)}
.fleet-img{position:absolute;left:32px;top:41px;width:388px;height:291px;background:linear-gradient(180deg,#8fb3d8 0%,#b4b9b8 45%,#a27a5a 100%)}
.fleet-text{position:absolute;left:463px;top:36px;width:423px}
.fleet-text .copy{margin-top:24px}
.fleet-text .btn{margin-top:30px}
.arrow{position:absolute;top:1570px}

/* contact */
.contact{position:absolute;top:1848px;left:0;width:1200px;height:372px;background:linear-gradient(90deg,#3a3f8a 0%,#2a2e80 30%,#23267a 60%,#3d3f7e 100%)}
.contact h2{position:absolute;top:32px;width:100%;text-align:center;color:var(--gold);font-size:33px;font-weight:700}
.field{position:absolute;height:36px;background:#fff;border-radius:3px;font-size:11.5px;font-weight:300;color:#777;padding:12px 12px}
.submit{position:absolute;left:533px;top:290px;width:134px;height:42px;background:var(--gold);color:#fff;font-size:11px;font-weight:600;display:flex;align-items:center;justify-content:center}

/* partners */
.partners{position:absolute;top:2220px;left:0;width:1200px;height:167px;background:#fff;display:flex;align-items:center;justify-content:space-around;padding:0 0}
.partner{background:#d9d9de;border-radius:6px}

/* map */
.directions{position:absolute;top:2387px;left:0;width:1200px;height:437px;background:var(--mist)}
.directions h2{position:absolute;top:45px;width:100%;text-align:center;font-size:27px}
.map{position:absolute;left:141px;top:87px;width:918px;height:308px;background:linear-gradient(135deg,#eef0f2 0%,#e6ebe4 50%,#edeef0 100%)}

/* footer */
.footer{position:absolute;top:2824px;left:0;width:1200px;height:259px;background:#fff}
.footer .brand{left:85px;top:112px}
.footer .brand .name{font-size:30px}
.footer .brand .mark{width:28px;height:28px}
.fcol{position:absolute;top:46px;font-size:12px;color:var(--navy);font-weight:400;line-height:25px;list-style:none}
.fcol h4{font-size:12.5px;font-weight:600;margin-bottom:1px}
.contact-list{position:absolute;left:996px;top:52px;font-size:11.5px;color:#666;line-height:15px}
.contact-list div{display:flex;gap:6px;margin-bottom:14px}
.contact-list h4{color:var(--navy);font-size:12.5px;font-weight:600;margin:8px 0 10px}
.contact-list .social i{background:var(--navy);width:16px;height:16px}
.contact-list .social{display:flex;gap:9px}
.bottombar{position:absolute;top:3083px;left:0;width:1200px;height:59px;background:var(--navy);color:#fff;font-size:11.5px;display:flex;align-items:center;justify-content:center}
</style>
</head>
<body>

<header class="topbar">
  <div class="info">
    <span><svg width="11" height="11" viewBox="0 0 24 24"><path fill="#fff" d="M6.6 10.8a15.1 15.1 0 0 0 6.6 6.6l2.2-2.2c.3-.3.7-.4 1-.2 1.1.4 2.3.6 3.6.6.6 0 1 .4 1 1V20c0 .6-.4 1-1 1A17 17 0 0 1 3 4c0-.6.4-1 1-1h3.5c.6 0 1 .4 1 1 0 1.3.2 2.5.6 3.6.1.3 0 .7-.2 1z"/></svg>Call <b>1300 442 019</b></span>
    <span class="sep"></span>
    <span><svg width="12" height="10" viewBox="0 0 24 18"><path fill="#fff" d="M0 0h24v2L12 9 0 2zM0 4l12 7 12-7v14H0z"/></svg></span>
    <span class="sep"></span>
    <span><svg width="9" height="12" viewBox="0 0 16 22"><path fill="#fff" d="M8 0a8 8 0 0 0-8 8c0 6 8 14 8 14s8-8 8-14a8 8 0 0 0-8-8zm0 11a3 3 0 1 1 0-6 3 3 0 0 1 0 6z"/></svg>18 Wattlegrove Rd, Kelsey QLD 4210</span>
  </div>
  <div class="social"><i></i><i></i><i></i><i></i><i></i></div>
</header>

<nav class="nav">
  <div class="brand"><span class="mark"></span><span class="name">BWR</span></div>
  <ul class="menu">
    <li class="active">HOME</li><li>ABOUT US</li><li>PLANT HIRE ▾</li><li>MAJOR PROJECT SNAPSHOT</li><li>POLICIES</li><li>JOBS</li><li>CONTACT US</li>
  </ul>
</nav>

<section class="hero">
  <div role="img" aria-label="Photo of yellow hire excavators lined up in a yard under blue sky" style="position:absolute;inset:0"></div>
  <div class="shade"></div>
  <h1>BWR HEAVY EQUIPMENT HIRE</h1>
  <p>Committed to superior quality plant hire services.</p>
  <div class="cta">GET A FREE QUOTE</div>
  <div class="dots">
    <svg width="8" height="14" viewBox="0 0 8 14"><path d="M7 1 1 7l6 6" stroke="#fff" stroke-width="1.5" fill="none"/></svg>
    <i></i><i class="on"></i><i></i><i></i><i></i>
    <svg width="8" height="14" viewBox="0 0 8 14"><path d="m1 1 6 6-6 6" stroke="#fff" stroke-width="1.5" fill="none"/></svg>
  </div>
</section>

<section>
  <div class="about-img" role="img" aria-label="Photo of a yellow excavator digging into a sand pile"></div>
  <div class="about-text">
    <h2>ABOUT US</h2>
    <p class="copy">Brambleworth Heavy Equipment Hire specialise in the hire of heavy earthmoving, mining and construction machines with specialised attachments and tooling. Our array of machines and attachments is second to none, and we have one of the largest hire fleets available in South East Queensland. If its plant hire you require, then Brambleworth Resources, or BWR as the local's call us – should be the first call you make. Wet or dry hire, we provide excellent operators and quality machines across all makes and models to guarantee you maximum up-time.</p>
    <p class="copy">We employ a group of highly skilled and capable managers who have worked throughout construction sites in Queensland, NSW and other parts of Australia to deliver a vast array of plant and equipment to mining, civil, building and industrial projects. Our expertise is applied to every project to ensure delivery is achieved in accordance with project specifications, productivity and cost targets. We offer plant hire and civil construction services from Brisbane to the Surat Basin, Gold Coast, Sunshine Coast, Capricorn Coast, south to Ballina, Coffs Harbour, then through to Gladstone, Ipswich and Toowoomba. Brambleworth Resources has Queensland covered!</p>
    <span class="btn">KNOW MORE</span>
  </div>
</section>

<section class="stats">
  <div class="stat-card">
    <div class="stat"><span class="icon" role="img" aria-label="Team icon"></span><div class="num"><b>20+</b><span>YEARS OF<br>EXPERIENCE</span></div></div>
    <div class="stat"><span class="icon" role="img" aria-label="Excavator icon"></span><div class="num"><b>100+</b><span>MACHINES<br>IN FLEET</span></div></div>
    <div class="stat"><span class="icon" role="img" aria-label="Queensland map icon"></span><span>ONE OF QLD'S LARGEST<br>SUPPLIERS</span></div>
    <div class="stat"><span class="icon" role="img" aria-label="Service worker icon"></span><span>ONSITE SERVICING<br>&nbsp;</span></div>
    <div class="stat"><span class="icon" role="img" aria-label="Auger attachment icon"></span><span>CUSTOM MACHINE<br>ATTACHMENTS</span></div>
  </div>
</section>

<section>
  <div class="tabs"><span>EXCAVATORS</span><span>DOZERS</span><span>DUMP TRUCKS</span><span>GRADERS</span><span>LOADERS</span><span>BOBCATS</span><span>WATER CARTS</span><span>BACKHOES</span><span>COMPACTORS</span></div>
  <svg class="arrow" style="left:92px" width="24" height="44" viewBox="0 0 24 44"><path d="M22 2 3 22l19 20" stroke="#bbb" stroke-width="3" fill="none"/></svg>
  <svg class="arrow" style="left:1084px" width="24" height="44" viewBox="0 0 24 44"><path d="m2 2 19 20L2 42" stroke="#bbb" stroke-width="3" fill="none"/></svg>
  <article class="fleet">
    <div class="fleet-img" role="img" aria-label="Photo of an orange excavator working on an urban site"></div>
    <div class="fleet-text">
      <h2>EXCAVATORS HIRE</h2>
      <p class="copy">With one of the largest fleet of excavators for hire in South East Queensland, at BWR Heavy Equipment we are proud of our large range of diggers. All our excavators and diggers for hire are sourced from reputable brands such as Ardent, Kestrel, Norrland, Daewha, Hikoru and more. We also have specialist machines – such as wheeled excavators for hire, long-reach and chameleon clamshell telescopic excavator upon request. We also have an impressive range of attachments and buckets.</p>
      <span class="btn">READ MORE</span>
    </div>
  </article>
</section>

<section class="contact">
  <div role="img" aria-label="Illustration of earthmoving machines in orange tones" style="position:absolute;inset:0;background:linear-gradient(90deg,rgba(180,120,70,.35) 0%,rgba(35,38,122,0) 28%,rgba(35,38,122,0) 68%,rgba(180,120,70,.35) 100%)"></div>
  <h2>CONTACT US TODAY FOR A FREE QUOTE</h2>
  <div class="field" style="left:346px;top:99px;width:249px">First Name*</div>
  <div class="field" style="left:605px;top:99px;width:249px">Last Name*</div>
  <div class="field" style="left:346px;top:149px;width:249px">Email Address*</div>
  <div class="field" style="left:605px;top:149px;width:249px">Mobile Number*</div>
  <div class="field" style="left:346px;top:199px;width:508px;height:57px">Your Massage...</div>
  <div class="submit">SUBMIT</div>
</section>

<section class="partners">
  <span class="partner" style="width:20px;height:76px"></span>
  <span class="partner" style="width:104px;height:80px"></span>
  <span class="partner" style="width:114px;height:70px"></span>
  <span class="partner" style="width:178px;height:58px"></span>
  <span class="partner" style="width:158px;height:44px"></span>
  <span class="partner" style="width:100px;height:80px"></span>
  <span class="partner" style="width:60px;height:64px"></span>
</section>

<section class="directions">
  <h2>GET DIRECTION TO REACH US</h2>
  <div class="map" role="img" aria-label="Street map showing the yard location in Kelsey">
    <svg width="918" height="308" style="position:absolute;inset:0"><circle cx="459" cy="142" r="8" fill="#e33"/></svg>
  </div>
</section>

<footer class="footer">
  <div class="brand"><span class="mark"></span><span class="name">BWR PLANT HIRE</span></div>
  <ul class="fcol" style="left:383px"><h4>NAVIGATION</h4><li>Home</li><li>About us</li><li>Machine Operator Jobs</li><li>Plant Hire</li><li>Attachments Hire</li><li>Policies</li></ul>
  <ul class="fcol" style="left:611px"><h4>PLANT HIRE</h4><li>Articulated Dump Trucks Hire</li><li>Dozer Hire</li><li>Excavator Diggers Hire</li><li>Grader Hire</li><li>Attachments Hire</li></ul>
  <ul class="fcol" style="left:805px"><h4>&nbsp;</h4><li>Backhoe Hire</li><li>Compactors Hire</li><li>Loader Hire</li><li>Skid Steer Hire</li><li>Water Cart Hire</li></ul>
  <div class="contact-list">
    <div><svg width="14" height="14" viewBox="0 0 24 24"><path fill="#23267a" d="M6.6 10.8a15.1 15.1 0 0 0 6.6 6.6l2.2-2.2c.3-.3.7-.4 1-.2 1.1.4 2.3.6 3.6.6.6 0 1 .4 1 1V20c0 .6-.4 1-1 1A17 17 0 0 1 3 4c0-.6.4-1 1-1h3.5c.6 0 1 .4 1 1 0 1.3.2 2.5.6 3.6.1.3 0 .7-.2 1z"/></svg>Call 1300 442 019</div>
    <div><svg width="11" height="15" viewBox="0 0 16 22"><path fill="#23267a" d="M8 0a8 8 0 0 0-8 8c0 6 8 14 8 14s8-8 8-14a8 8 0 0 0-8-8zm0 11a3 3 0 1 1 0-6 3 3 0 0 1 0 6z"/></svg>18 Wattlegrove Rd,<br>Kelsey QLD 4210</div>
    <h4>FOLLOW US</h4>
    <div class="social"><i></i><i></i><i></i><i></i><i></i></div>
  </div>
</footer>
<div class="bottombar">2024© All right reserved by BWR</div>

</body>
</html>
```